Postcard Design for Thank Yous

I am a Voice Actor and want to send personal thank you cards or postcards to clients after recording sessions. the basic concept is front art that simply has background art & my logo (sample below but wrong size), and the other side would be space for mailing address as well as a small version of my logo and contact info and of course plenty of blank space for me to write a personal message. I am open to your opinion as to whether a postcard, or a card and mailing envelope makes more sense. (I am also including the back of business card as example of contact listing, but one number will not be included and I might want to change other verbiage). Thank you! -Neil

```html
<!DOCTYPE html>
<html lang="en">
<head>
<meta charset="utf-8">
<title>Neil Halvorsen – Voice Actor Postcard</title>
<link href="https://fonts.googleapis.com/css2?family=Open+Sans:ital,wght@0,400;0,700;1,700;1,800&display=swap" rel="stylesheet">
<style>
  :root {
    --stage: #d9d9d9;
    --stage-edge: #9a9a9a;
    --band: #3e3f44;
    --photo-dark: #2b2a28;
    --photo-mid: #6d6a65;
    --paper: #ffffff;
    --paper-fade: #cfcfcf;
    --accent: #e0201b;
    --ink: #1c1c1c;
    --white: #ffffff;
  }
  * { margin: 0; padding: 0; box-sizing: border-box; }
  html, body { width: 1200px; height: 900px; overflow: hidden; }
  body {
    background: radial-gradient(ellipse at 50% 40%, var(--stage) 0%, var(--stage-edge) 100%);
    font-family: "Open Sans", Arial, sans-serif;
    position: relative;
  }
  .postcard {
    position: absolute;
    width: 615px;
    height: 410px;
    overflow: hidden;
    box-shadow: 0 6px 18px rgba(0,0,0,.35);
  }

  /* Message side */
  .postcard--message { left: 90px; top: 30px; background: var(--paper); }
  .message-art {
    position: absolute; left: 0; top: 0; width: 100%; height: 100%;
    background: linear-gradient(90deg, var(--photo-mid) 0%, var(--paper-fade) 40%, var(--paper) 68%);
    opacity: .8;
  }
  .contact-block {
    position: absolute; left: 14px; top: 12px;
    display: flex; gap: 8px; align-items: flex-start;
    font-size: 7.5px; line-height: 10px; color: var(--ink);
  }
  .brand-mark {
    display: flex; flex-direction: column; align-items: center; gap: 3px;
    background: var(--ink); padding: 4px; width: 78px;
  }
  .brand-mark__square { width: 44px; height: 34px; background: var(--accent); }
  .brand-mark__name { font-size: 6px; font-weight: 700; color: var(--white); line-height: 8px; }
  .contact-list { list-style: none; font-weight: 700; }
  .contact-list .contact-name { color: var(--accent); }
  .contact-list .tag { color: var(--accent); }
  .social-row {
    position: absolute; left: 14px; top: 76px;
    display: flex; gap: 26px; font-size: 7.5px; font-weight: 700; color: var(--ink);
  }
  .social-row span { display: flex; align-items: center; gap: 4px; }
  .social-row i { width: 8px; height: 8px; border-radius: 50%; background: var(--band); display: inline-block; }

  /* Art side */
  .postcard--art { left: 495px; top: 460px; background: var(--band); }
  .art-shape { position: absolute; inset: 0; }
  .site-url {
    position: absolute; left: 150px; top: 26px;
    transform: rotate(8.5deg); transform-origin: left top;
    font-style: italic; font-weight: 800; font-size: 27px; letter-spacing: .5px;
    color: var(--white); text-shadow: 1px 1px 2px rgba(0,0,0,.6);
  }
  .art-logo {
    position: absolute; left: 16px; top: 240px;
    display: flex; align-items: center; gap: 8px;
  }
  .art-logo__square { width: 30px; height: 30px; background: var(--accent); }
  .art-logo__name { font-weight: 700; font-size: 14px; color: var(--white); }
  .signature-line {
    position: absolute; right: 16px; bottom: 14px;
    transform: rotate(8.5deg); transform-origin: right bottom;
    font-style: italic; font-weight: 800; font-size: 17px;
    color: var(--white); text-shadow: 1px 1px 2px rgba(0,0,0,.6);
  }
  .signature-line .dash { color: var(--accent); }
</style>
</head>
<body>

  <section class="postcard postcard--message">
    <div class="message-art" role="img" aria-label="Faded black and white photo of a cocktail glass and poker chips"></div>
    <div class="contact-block">
      <div class="brand-mark">
        <span class="brand-mark__square"></span>
        <span class="brand-mark__name">Neil Halvorsen</span>
      </div>
      <ul class="contact-list">
        <li class="contact-name">Neil Halvorsen - Voice Actor</li>
        <li>Remote Link / ISDN Bridge</li>
        <li>555.014.2830 <span class="tag">(Main)</span></li>
        <li>555.019.7713 <span class="tag">(studio)</span></li>
        <li>www.neilhalvorsenvoice.com</li>
        <li>Neil@NeilHalvorsenVoice.com</li>
      </ul>
    </div>
    <div class="social-row">
      <span><i></i>neilhalvorsen</span>
      <span><i></i>neil.halvorsen</span>
    </div>
  </section>

  <section class="postcard postcard--art">
    <svg class="art-shape" width="615" height="410" viewBox="0 0 615 410">
      <defs>
        <radialGradient id="tableTone" cx="45%" cy="45%" r="70%">
          <stop offset="0" stop-color="#8a8680"/>
          <stop offset=".6" stop-color="#4e4b47"/>
          <stop offset="1" stop-color="#1f1e1c"/>
        </radialGradient>
      </defs>
      <path d="M0,0 L150,0 C320,12 470,50 615,88 L615,360 C450,330 250,290 0,178 Z"
            fill="url(#tableTone)" role="img"
            aria-label="Black and white photo of playing cards and poker chips on a table"/>
      <path d="M150,0 C320,12 470,50 615,88" fill="none" stroke="#ffffff" stroke-width="2"/>
      <path d="M0,178 C250,290 450,330 615,360" fill="none" stroke="#ffffff" stroke-width="2"/>
    </svg>
    <div class="site-url">www.neilhalvorsenvoice.com</div>
    <div class="art-logo">
      <span class="art-logo__square"></span>
      <span class="art-logo__name">Neil Halvorsen</span>
    </div>
    <div class="signature-line">Neil Halvorsen <span class="dash">-</span> Voice Actor</div>
  </section>

</body>
</html>
```